Business card design for sports medicine and athlete care clinic.

We need a bold, solid business card design for our practitioners to stand out. We treat overuse & sports-related injuries and provide post-operative rehabilitation. Our specialisations include chronic conditions, men’s health, nutrition & musculoskeletal disorders (MSDs). All brand collateral in terms of fonts, logo and colour palette to be provided.

Target Market(s)

Athletes (professional and amateur), sportspeople, predominantly male

Industry/Entity Type

Health And Wellness

Contact Information for Business Card

The front of the card should be white with dark blue text the back dark blue with white text. The logo should be top-left. The business name should be horizontal and right of the logo. The tagline should be directly below centred on the back of the card (see top-banner.png and bottom-banner.png)

Font styles to use
Sans Serif

Colors
0355a3
0293ce
3176b5
ffffff
85acd3

Requirements
Nice to have
• Diagonal and/or horizontal line elements between logo and practitioner details and/or bottom corner of card (see slide.png and tag-bg.png).

```html
<!DOCTYPE html>
<html lang="en">
<head>
<meta charset="utf-8">
<title>Stridewell Clinic – Business Card</title>
<link rel="stylesheet" href="https://fonts.googleapis.com/css2?family=Montserrat:ital,wght@0,400;0,600;0,700;1,500&display=swap">
<style>
  :root {
    --bg: #8c8c8c;
    --card: #e9e9ec;
    --navy: #0d1148;
    --blue: #0355a3;
    --sky: #0293ce;
    --pale: #85acd3;
    --white: #ffffff;
    --ink: #1b2150;
    --emboss-hi: #fafafc;
    --emboss-lo: #d3d3da;
  }
  * { margin: 0; padding: 0; box-sizing: border-box; }
  html, body { width: 1200px; height: 1200px; overflow: hidden; }
  body {
    background: var(--bg);
    font-family: "Montserrat", Arial, sans-serif;
    position: relative;
  }
  .card {
    position: absolute;
    top: 209px;
    width: 410px;
    height: 738px;
    background: var(--card);
    box-shadow: 18px 14px 30px rgba(0, 0, 0, 0.25);
  }
  .card--front { left: 112px; }
  .card--back { left: 672px; background: var(--navy); }

  .runner-art {
    position: absolute;
    left: 0; top: 0;
    width: 410px; height: 387px;
    background:
      linear-gradient(135deg, var(--emboss-hi) 0%, var(--emboss-lo) 45%, var(--emboss-hi) 70%, var(--emboss-lo) 100%);
    opacity: 0.85;
  }
  .holder {
    position: absolute;
    left: 96px; top: 458px;
  }
  .holder__name {
    font-weight: 700;
    font-size: 27px;
    color: var(--blue);
    line-height: 1.1;
  }
  .holder__role {
    font-size: 16px;
    color: var(--ink);
    margin-top: 2px;
  }
  .contacts {
    list-style: none;
    margin-top: 38px;
  }
  .contacts li {
    display: flex;
    align-items: center;
    gap: 6px;
    font-size: 16px;
    color: var(--ink);
    height: 24px;
  }
  .contacts svg { width: 14px; height: 14px; fill: var(--blue); flex: none; }

  .brand {
    position: absolute;
    left: 36px; top: 548px;
    display: flex;
    align-items: center;
    gap: 14px;
  }
  .card--back .brand { top: 339px; }
  .brand__dot {
    width: 58px; height: 58px;
    border-radius: 50%;
    background: var(--sky);
    flex: none;
  }
  .brand__name {
    font-weight: 700;
    font-size: 27px;
    color: var(--white);
    line-height: 1;
  }
  .brand__tagline {
    font-style: italic;
    font-weight: 500;
    font-size: 12.5px;
    color: var(--white);
    letter-spacing: 0.6px;
    margin-top: 8px;
  }
</style>
</head>
<body>
  <section class="card card--front">
    <div class="runner-art" role="img" aria-label="Blind-embossed illustration of a sprinting athlete with muscle outlines"></div>
    <div class="holder">
      <p class="holder__name">Lukas Reinhart</p>
      <p class="holder__role">Director</p>
      <ul class="contacts">
        <li>
          <svg viewBox="0 0 14 14"><path d="M3.5 0h7a1 1 0 0 1 1 1v12a1 1 0 0 1-1 1h-7a1 1 0 0 1-1-1V1a1 1 0 0 1 1-1zm.5 1.5v9.5h6V1.5zM7 11.6a.8.8 0 1 0 0 1.6.8.8 0 0 0 0-1.6z"/></svg>
          +41 70 123 45 67
        </li>
        <li>
          <svg viewBox="0 0 14 14"><path d="M3 1l2 3-1.3 1.3a8 8 0 0 0 5 5L10 9l3 2-1.2 2.2C6.5 13.5.5 7.5.8 2.2z"/></svg>
          +43 660 555 01 234
        </li>
        <li>
          <svg viewBox="0 0 14 14"><path d="M0 3h14v1.2L7 8.5 0 4.2zM0 5.6l7 4.3 7-4.3V12H0z"/></svg>
          hello@stridewellclinic.com
        </li>
        <li>
          <svg viewBox="0 0 14 14"><path d="M7 0a7 7 0 1 0 0 14A7 7 0 0 0 7 0zm0 1.5a5.5 5.5 0 0 1 4.6 2.5H9.5L8 5.5 9 7l-1 2-1.5.5-.5 2.5A5.5 5.5 0 0 1 2 4.5l2 .5 1.5 1.5L5 4l1.5-2z"/></svg>
          www.stridewellclinic.com
        </li>
      </ul>
    </div>
  </section>

  <section class="card card--back">
    <div class="brand">
      <span class="brand__dot" aria-hidden="true"></span>
      <div>
        <p class="brand__name">Stridewell Clinic</p>
        <p class="brand__tagline">Sports medicine and athlete care</p>
      </div>
    </div>
  </section>
</body>
</html>
```